Web Design Project

i'm looking for a sleek modern design i can use for a web site that deals with.
Intelligent Data Capture
Accounts Payable Solutions for faster processing based on our scanning solution.
ultimately we are a intelligent scanning software.

here is a great website, that does exactly what we do, and we like to have most of their services and products.

so something in this idea would be great.
www.dravolin.com

so i guess i want a good landing/home page which is smartly designed so users will be inclined to leave their information.

and then information pages.

also i dont need any cms for you to include, i only need you to hook the html hooks for RANK Kettle as i already have a CMS and need it to hook in to that, i am including links to that cheat sheet.
so it is easier when included as you create the Theme.

http://www.rankkettle.com/how-to-create-website-template.html
http://www.rankkettle.com/cheat-sheet.html
Updates

Hi Guys sorry for the long pause in design, but here is where we stand.

what ever design i choose, i need that designer to customize a few things for me based on design that was designed.
and i will need designer to match that them to work with RANK Kettle
here is the cheat sheet for the hooks that we need to match and make it work.
if you have any questions let me know.

otherwise i look forward to working with you. and good luck.

Target Market(s)

CFO's AP Managers, mostly ppl who are not Tech freindly

Industry/Entity Type

Software

Requirements
Must have
• i need on home page, the rotating banner should have 1 ability to place vidmora links to show videos, and also ability to add buttons on these rotating banners that will allow forms to pop up take to another page.

```html
<!DOCTYPE html>
<html lang="en">
<head>
<meta charset="utf-8">
<title>Company — Data Capture Solutions</title>
<link href="https://fonts.googleapis.com/css2?family=Arimo:wght@400;700&family=Didact+Gothic&family=Ubuntu:wght@700&family=Rosario&display=swap" rel="stylesheet">
<style>
:root{
  --page:#f1f1f1;
  --ink:#111;
  --navy:#2a4a6b;
  --blue-dark:#0a5f96;
  --blue:#1a8bc8;
  --blue-light:#3fb2e6;
  --nav-top:#4a4a4a;
  --nav-bot:#1f1f1f;
  --red:#b8210f;
  --footer:#000;
  --footer-text:#9a9a9a;
  --footer-line:#2c2c2c;
  --white:#fff;
}
*{box-sizing:border-box;margin:0;padding:0}
html,body{width:834px;height:1200px;overflow:hidden}
body{background:var(--page);font-family:"Arimo",Arial,sans-serif;color:var(--ink);position:relative}
.abs{position:absolute}

/* header */
.site-header{left:0;top:0;width:834px;height:87px;background:var(--white)}
.brand{left:30px;top:20px}
.brand-name{font-family:"Arimo",Arial,sans-serif;font-weight:700;font-size:22px;color:var(--navy);letter-spacing:1px}
.brand-tag{font-family:"Arimo",Arial,sans-serif;font-size:13px;color:#333;margin-top:16px;letter-spacing:.3px}
.search{left:565px;top:10px;width:260px;height:42px;background:linear-gradient(#3a3a3a,#111);border-radius:6px;padding:7px}
.search-field{width:215px;height:26px;background:linear-gradient(#fff,#e6e6e6);border-radius:2px;font-size:10px;color:#333;padding:8px 10px}
.search-icon{position:absolute;right:8px;top:8px}

/* nav */
.main-nav{left:0;top:87px;width:834px;height:32px;background:linear-gradient(var(--nav-top),var(--nav-bot));display:flex;padding-left:262px;border-top:1px solid #777}
.nav-item{height:31px;display:flex;align-items:center;justify-content:center;color:var(--white);font-weight:700;font-size:13px;border-right:1px solid #111;box-shadow:1px 0 0 #555}
.nav-item.is-active{background:linear-gradient(#d0321c,var(--red))}

/* hero */
.hero{left:0;top:119px;width:834px;height:301px;background:radial-gradient(ellipse at 60% 20%,var(--blue-light),var(--blue) 45%,var(--blue-dark));border-bottom:4px solid #1b1b1b}
.hero-text{font-family:"Ubuntu",Arial,sans-serif;color:var(--white);text-shadow:2px 2px 3px rgba(0,0,0,.55);font-weight:700;white-space:nowrap}
.hero-kicker{left:20px;top:45px;font-size:22px}
.hero-line{font-size:41px}
.hero-people{left:482px;top:98px;width:317px;height:203px;background:linear-gradient(180deg,rgba(40,40,50,.25),rgba(30,30,36,.75));border-radius:60px 60px 0 0}

/* feature boxes */
.feature{top:437px;height:166px;background:linear-gradient(#1e90cc,#0a6aa8);color:var(--white);text-align:center;font-family:"Arimo",Arial,sans-serif}
.feature-title{font-family:"Ubuntu",Arial,sans-serif;font-size:21px;margin-top:8px;padding-bottom:6px;border-bottom:1px solid rgba(255,255,255,.35);margin-left:20px;margin-right:12px}
.feature-body{font-size:15px;line-height:16px;margin-top:8px}
.read-more{display:inline-flex;align-items:center;gap:6px;margin-top:13px;width:118px;height:28px;justify-content:center;background:linear-gradient(#3c3c3c,#0e0e0e);border-radius:3px;font-size:10px;font-weight:700;color:var(--white);box-shadow:0 1px 2px rgba(0,0,0,.5)}
.divider{left:20px;top:617px;width:798px;height:2px;background:#d4d4d4}

/* welcome */
.welcome-title{left:39px;top:644px;font-size:21px;font-weight:700}
.welcome-copy{left:26px;width:384px;font-family:"Didact Gothic",Arial,sans-serif;font-size:12.4px;line-height:15.6px;text-align:center;color:#111}

/* video */
.player{left:439px;top:662px;width:373px;height:272px;background:linear-gradient(#2a2a2a,#0d0d0d);box-shadow:0 30px 24px -18px rgba(0,0,0,.35)}
.player-screen{position:absolute;left:15px;top:15px;width:345px;height:192px;background:radial-gradient(ellipse at 40% 20%,#7fc6ea,#2d8fcc 60%,#1a6faa);border:2px solid #000}
.player-play{position:absolute;left:133px;top:66px}
.player-bar{position:absolute;left:0;top:224px;width:373px;height:44px;background:linear-gradient(#2c3a46,#11161a)}
.ctrl{position:absolute;top:11px;width:24px;height:22px;background:linear-gradient(#3b4a57,#1a2229);border-radius:2px}
.time{position:absolute;left:183px;top:17px;font-size:8px;color:#ddd;font-family:Arial,sans-serif}

/* footer */
.site-footer{left:0;top:988px;width:834px;height:212px;background:var(--footer);border-top:3px solid #333}
.f-title{font-weight:700;font-size:21px;color:var(--white)}
.f-list{list-style:none;font-family:"Rosario",Arial,sans-serif;font-size:12px;color:var(--footer-text);letter-spacing:.4px}
.f-list li{height:27px;border-top:1px solid var(--footer-line);display:flex;align-items:center}
.f-list li:last-child{border-bottom:1px solid var(--footer-line)}
.f-label{width:52px}
.f-mail{color:#ddd;text-decoration:underline}
.f-sq{width:13px;height:13px;border-radius:2px;margin-left:-20px;margin-right:7px}
.f-chev{margin-left:-11px;margin-right:6px;color:#777;font-size:10px}
.news-input{left:626px;top:66px;width:184px;height:28px;background:var(--white);font-family:"Rosario",Arial,sans-serif;font-style:italic;font-size:12px;color:#aaa;padding:7px 14px}
.subscribe{left:735px;top:102px;width:75px;height:29px;background:var(--white);font-size:13px;color:#111;display:flex;align-items:center;justify-content:center}
</style>
</head>
<body>

<header class="site-header abs">
  <div class="brand abs">
    <div class="brand-name">COMPANY</div>
    <div class="brand-tag">Data Capture Solutions</div>
  </div>
  <div class="search abs">
    <div class="search-field">search...</div>
    <svg class="search-icon" width="22" height="24" viewBox="0 0 22 24"><circle cx="9" cy="9" r="6.5" fill="none" stroke="#fff" stroke-width="3"/><line x1="13.5" y1="14" x2="19" y2="21" stroke="#fff" stroke-width="4" stroke-linecap="round"/></svg>
  </div>
</header>

<nav class="main-nav abs">
  <div class="nav-item is-active" style="width:87px">HOME</div>
  <div class="nav-item" style="width:95px">ABOUT US</div>
  <div class="nav-item" style="width:92px">PRODUCT</div>
  <div class="nav-item" style="width:102px">INDUSTRIES</div>
  <div class="nav-item" style="width:87px">CONTACT</div>
  <div class="nav-item" style="width:89px">LOGIN</div>
</nav>

<section class="hero abs" role="img" aria-label="Blue banner with a faint world map behind the headline">
  <div class="hero-text hero-kicker abs">A Leading Provider for</div>
  <div class="hero-text hero-line abs" style="left:108px;top:102px">Data Capture</div>
  <div class="hero-text hero-line abs" style="left:224px;top:158px">&amp;</div>
  <div class="hero-text hero-line abs" style="left:30px;top:216px">Document Recognition</div>
  <div class="hero-people abs" role="img" aria-label="Photo of a team of business people in suits standing together"></div>
</section>

<article class="feature abs" style="left:34px;width:228px">
  <h2 class="feature-title">Professionals</h2>
  <p class="feature-body">Lorem ipsum dolor<br>sit amet, consec teteur<br>adipiscing elit.<br>Praesent vestibulum</p>
  <span class="read-more"><svg width="10" height="7"><ellipse cx="5" cy="4" rx="5" ry="3" fill="#555"/></svg>Read More &gt;</span>
</article>
<article class="feature abs" style="left:307px;width:229px">
  <h2 class="feature-title">Strategies</h2>
  <p class="feature-body">Lorem ipsum dolor<br>sit amet, consec teteur<br>adipiscing elit.<br>Praesent vestibulum</p>
  <span class="read-more"><svg width="10" height="7"><ellipse cx="5" cy="4" rx="5" ry="3" fill="#555"/></svg>Read More &gt;</span>
</article>
<article class="feature abs" style="left:567px;width:230px">
  <h2 class="feature-title">Solutions</h2>
  <p class="feature-body">Lorem ipsum dolor<br>sit amet, consec teteur<br>adipiscing elit.<br>Praesent vestibulum</p>
  <span class="read-more"><svg width="10" height="7"><ellipse cx="5" cy="4" rx="5" ry="3" fill="#555"/></svg>Read More &gt;</span>
</article>

<div class="divider abs"></div>

<h1 class="welcome-title abs">Welcome !</h1>
<p class="welcome-copy abs" style="top:686px">Lorem ipsum dolor sit amet, consectetur adipisicing elit, sed do eiusmod tempor incididunt ut labore et dolore magna aliqua. Ut enim ad minim veniam, quis nostrud exercitation ullamco laboris nisi ut aliquip ex ea commodo consequat. Duis aute irure dolor in reprehenderit in voluptate. Lorem ipsum dolor sit amet, consectetur adipisicing elit, sed do eiusmod tempor.</p>
<p class="welcome-copy abs" style="top:811px">Lorem ipsum dolor sit amet, consectetur adipisicing elit, sed do eiusmod tempor incididunt ut labore et dolore magna aliqua. Ut enim ad minim veniam, quis nostrud exercitation ullamco laboris nisi ut aliquip ex ea commodo consequat. Duis aute irure dolor in reprehenderit in voluptate. Lorem ipsum dolor sit amet, consectetur adipisicing elit, sed do eiusmod tempor inci-didunt ut labore et dolo.</p>

<div class="player abs">
  <div class="player-screen">
    <svg class="player-play" width="70" height="70" viewBox="0 0 70 70"><circle cx="35" cy="35" r="33" fill="#e4e4e4" stroke="#bbb" stroke-width="2"/><path d="M27 20 L50 35 L27 50 Z" fill="#555"/></svg>
  </div>
  <div class="player-bar">
    <div class="ctrl" style="left:28px"><svg width="24" height="22"><rect x="8" y="7" width="8" height="8" fill="#2fa3e6"/></svg></div>
    <div class="ctrl" style="left:56px"><svg width="24" height="22"><rect x="8" y="6" width="3" height="10" fill="#2fa3e6"/><rect x="13" y="6" width="3" height="10" fill="#2fa3e6"/></svg></div>
    <svg class="abs" style="left:90px;top:19px" width="76" height="6"><rect width="76" height="6" fill="#000"/><rect width="3" height="6" fill="#c22"/></svg>
    <span class="time">00:01 / 00:29</span>
    <div class="ctrl" style="left:264px;width:32px"><svg width="32" height="22"><g fill="#fff"><rect x="7" y="8" width="2" height="6"/><rect x="11" y="8" width="2" height="6"/><rect x="15" y="8" width="2" height="6"/><rect x="19" y="8" width="2" height="6"/><rect x="23" y="8" width="2" height="6"/></g></svg></div>
    <div class="ctrl" style="left:318px;width:32px"><svg width="32" height="22" fill="none" stroke="#fff" stroke-width="1.5"><path d="M10 9V6h3M22 9V6h-3M10 13v3h3M22 13v3h-3"/></svg></div>
  </div>
</div>

<footer class="site-footer abs">
  <h3 class="f-title abs" style="left:25px;top:20px">Why US</h3>
  <ul class="f-list abs" style="left:32px;top:54px;width:155px">
    <li><span class="f-chev">›</span>Lorem ipsum dolor sit</li>
    <li><span class="f-chev">›</span>Dmet, consectetur</li>
    <li><span class="f-chev">›</span>Adipisicing elit eiusmod</li>
    <li><span class="f-chev">›</span>Tempor incididunt ut</li>
  </ul>

  <h3 class="f-title abs" style="left:247px;top:23px">Address</h3>
  <ul class="f-list abs" style="left:230px;top:55px;width:168px;padding-left:3px">
    <li><span>Country:&nbsp; ARDENIA</span></li>
    <li><span class="f-label">City:</span>LUMERA</li>
    <li><span class="f-label">Phone:</span>8 800 210-37-94</li>
    <li><span class="f-label">Email:</span><span class="f-mail">hello@capturely.co</span></li>
  </ul>

  <h3 class="f-title abs" style="left:445px;top:24px">Follow Us</h3>
  <ul class="f-list abs" style="left:456px;top:55px;width:144px;padding-left:2px">
    <li><span class="f-sq" style="background:#3a5a98"></span>Friendnest</li>
    <li><span class="f-sq" style="background:#39a9e0"></span>Chirpline</li>
    <li><span class="f-sq" style="background:#1b72b0"></span>ProNetwork</li>
    <li><span class="f-sq" style="background:#ccc"></span>Markstash</li>
  </ul>

  <h3 class="f-title abs" style="left:627px;top:22px">News Letter</h3>
  <div class="news-input abs">Type Your Email Here</div>
  <div class="subscribe abs">Subscribe</div>
</footer>

</body>
</html>
```